Fennick Executive Search - New Business Card Design Project

We are an executive search firm called Fennick Executive Search based in the UK. We require a custom design for a business card. We're looking to convey a professional service to executives for executive search recruitment services. In terms of colours, we like dark blues and grays (maybe even silver incorporated somewhere if we go for a foiled type of card) but we're open to your artistic flare. See our current logo in attachments. We are totally open on design so long as the design is slick and professional.
Updates

Thanks for all your contributions of various designs. I have to say the quality of work has been amazing which is going to make our job quite difficult in the coming days on making a decision. Thanks to you all that have taken the time to submit designs thus far. We'll keep on reviewing and try to narrow down our selection as soon as possible.

Target Market(s)

Executive Search

Industry/Entity Type

Recruitment

Contact Information for Business Card

Fennick Executive Search,
Exclusively Sourcing & Hiring Senior Leaders
Gordon Pellbury, Managing Director,
07823 906417
0117 486 7132
gordon@fennickexecutive.co.uk
fennickexecutive.co.uk
58 Lindmoor Court, Hatherley Road, Bristol, BS32 9QJ

Font styles to use
Sans Serif
Other font styles liked:
• Roboto (which is used in our logo)

Requirements
Must have
• Our logo (It has a subtle fade on it from #02071d at top to #333649 at bottom)
• The logo can be on one side or both sides
• Must be elegant and professional
• We have 2nd slogan ADVISE | ENGAGE | EVOLVE | ACHIEVE which can be incorporated into the card
Nice to have
• Use of blues and grey colours
• Compatible with similar styling to our website fennickexecutive.co.uk
Should not have
• Must not be overly brash
• Must not contain cartoon characters

```html
<!DOCTYPE html>
<html lang="en">
<head>
<meta charset="utf-8">
<title>Fennick Executive Search – Business Card</title>
<link rel="stylesheet" href="https://fonts.googleapis.com/css2?family=Roboto:wght@300;400;500;700&display=swap">
<style>
  :root {
    --navy-top: #02071d;
    --navy-bottom: #333649;
    --silver-light: #e6e7e9;
    --silver-mid: #c4c5c8;
    --silver-dark: #a2a3a6;
    --ink-white: #ffffff;
    --rule: #3a3b40;
    --page: #f2f2f2;
  }
  * { margin: 0; padding: 0; box-sizing: border-box; }
  html, body { width: 960px; height: 1200px; overflow: hidden; }
  body {
    background: var(--page);
    font-family: "Roboto", Arial, sans-serif;
    position: relative;
  }
  .card {
    position: absolute;
    left: 150px;
    width: 659px;
    height: 407px;
    background: linear-gradient(110deg, var(--silver-light) 0%, var(--silver-mid) 55%, var(--silver-dark) 100%);
    overflow: hidden;
  }
  .card--front { top: 118px; }
  .card--back { top: 636px; }

  /* Front */
  .brand-band {
    position: absolute;
    left: 40px; top: 0;
    width: 224px; height: 100%;
    background: linear-gradient(180deg, var(--navy-top) 0%, var(--navy-bottom) 100%);
  }
  .brand-band__name {
    position: absolute;
    left: 27px; top: 172px;
    width: 190px;
    color: var(--ink-white);
    font-weight: 500;
    font-size: 20px;
    line-height: 1.3;
    letter-spacing: 0.3px;
    text-transform: uppercase;
  }
  .brand-band__rule {
    position: absolute;
    left: 20px; top: 232px;
    width: 180px; height: 1px;
    background: rgba(255,255,255,0.15);
  }
  .brand-band__slogan {
    position: absolute;
    left: 50px; top: 242px;
    color: var(--ink-white);
    font-size: 12px;
    font-weight: 400;
    line-height: 1.3;
  }
  .person {
    position: absolute;
    left: 297px; top: 58px;
    color: var(--ink-white);
  }
  .person__name {
    font-size: 21px;
    font-weight: 300;
    letter-spacing: 0.3px;
    text-transform: uppercase;
  }
  .person__name strong { font-weight: 700; }
  .person__role {
    font-size: 14px;
    font-weight: 300;
    letter-spacing: 4.3px;
    margin-top: -2px;
  }
  .divider {
    position: absolute;
    left: 288px;
    width: 308px; height: 1px;
    background: var(--rule);
  }
  .divider--top { top: 130px; }
  .divider--bottom { top: 222px; }
  .address {
    position: absolute;
    left: 297px; top: 153px;
    width: 300px;
    color: var(--ink-white);
    font-size: 15px;
    font-weight: 300;
    line-height: 21px;
    font-style: normal;
  }
  .contact-list {
    position: absolute;
    left: 288px; top: 250px;
    list-style: none;
    color: var(--ink-white);
    font-size: 15px;
    font-weight: 300;
  }
  .contact-list li {
    display: flex;
    align-items: center;
    gap: 8px;
    height: 20px;
  }
  .contact-list li.gap { margin-top: 12px; }
  .contact-list li.web { margin-top: 9px; }
  .contact-list svg { width: 15px; height: 14px; fill: var(--ink-white); flex: none; }

  /* Back */
  .back-name {
    position: absolute;
    left: 0; top: 222px;
    width: 100%;
    text-align: center;
    color: var(--navy-top);
    font-size: 22px;
    font-weight: 500;
    letter-spacing: 0.4px;
    text-transform: uppercase;
  }
  .back-slogan {
    position: absolute;
    left: 0; top: 284px;
    width: 100%;
    text-align: center;
    color: var(--ink-white);
    font-size: 17px;
    font-weight: 300;
    letter-spacing: 0.3px;
  }
</style>
</head>
<body>
  <section class="card card--front">
    <div class="brand-band">
      <p class="brand-band__name">Fennick<br>Executive Search</p>
      <div class="brand-band__rule"></div>
      <p class="brand-band__slogan">ADVISE | ENGAGE<br>EVOLVE | ACHIEVE</p>
    </div>

    <div class="person">
      <p class="person__name"><strong>Gordon</strong> Pellbury</p>
      <p class="person__role">Managing Director</p>
    </div>

    <div class="divider divider--top"></div>
    <address class="address">58 Lindmoor Court, Hatherley Road, Bristol, BS32 9QJ</address>
    <div class="divider divider--bottom"></div>

    <ul class="contact-list">
      <li>
        <svg viewBox="0 0 16 14" aria-hidden="true"><path d="M1 5c0-2 3-4 7-4s7 2 7 4l-3 1-1-2H5L4 6 1 5zM4 7h8l2 6H2l2-6zm4 1.5a2 2 0 100 4 2 2 0 000-4z"/></svg>
        07823 906417
      </li>
      <li>
        <svg viewBox="0 0 16 14" aria-hidden="true"><path d="M4 0h8v4H4zM1 5h14v6h-3v3H4v-3H1zM5 9v4h6V9z"/></svg>
        0117 486 7132
      </li>
      <li class="gap">
        <svg viewBox="0 0 16 12" aria-hidden="true"><path d="M0 0h16v12H0zm1.5 1.5v.4L8 7l6.5-5.1v-.4zm0 2.3v6.7h13V3.8L8 8.9z"/></svg>
        gordon@fennickexecutive.co.uk
      </li>
      <li class="web">
        <svg viewBox="0 0 16 14" aria-hidden="true"><path d="M0 0h16v10H0zm1.5 1.5v7h13v-7zM6 11h4v1.5h2V14H4v-1.5h2z"/></svg>
        fennickexecutive.co.uk
      </li>
    </ul>
  </section>

  <section class="card card--back">
    <p class="back-name">Fennick Executive Search</p>
    <p class="back-slogan">ADVISE | ENGAGE | EVOLVE | ACHIEVE</p>
  </section>
</body>
</html>
```